Brava Stone Oven Kitchen (restaurant)

Restaurant with a cool vibe.
We need a refresh of existing site. Appealing to a hip crowd of 25 or older age bracket (mid price to high small town). Constant changes food and cocktail menu. A vibing atmosphere with jazz funk hip music.
Must be able to scale for any device… phone/mobile device super important.
Instagram: @Brava.Linwell
Website: bravalinwell.example

Target Market(s)

25-55 age group

Number of Pages Required

1 page

Font styles to use
Sans Serif

Requirements
Must have
• Simple to navigate. Simplicity is the key to all sophistication.

Links/Buttons
Menu
Gift Cards
Reservations
Take Out
Contact Us
Should not have
• Please, nothing generic looking… no cookie cutter look. Originality

```html
<!DOCTYPE html>
<html lang="en">
<head>
<meta charset="utf-8">
<title>Brava Stone Oven Kitchen</title>
<link href="https://fonts.googleapis.com/css2?family=Exo+2:wght@500;600;700;800&family=Raleway:wght@400;500;600&family=Rye&display=swap" rel="stylesheet">
<style>
:root{
  --orange:#e8501f;
  --teal:#2fc6c0;
  --yellow:#f0b323;
  --ink:#1d1d1d;
  --text:#777;
  --dark:#1f1f1f;
  --white:#fff;
}
*{margin:0;padding:0;box-sizing:border-box}
html,body{width:1200px;height:4645px;overflow:hidden}
body{font-family:"Raleway",sans-serif;color:var(--ink);background:#fff;position:relative}
.abs{position:absolute}
.section{position:absolute;left:0;width:1200px}
.display{font-family:"Rye",serif;font-weight:400}
.head{font-family:"Exo 2",sans-serif}
.btn{position:absolute;display:flex;align-items:center;justify-content:center;font-family:"Raleway",sans-serif;font-size:12px;letter-spacing:1px;text-transform:uppercase;background:var(--orange);color:#fff}
.btn.light{background:#fff;color:var(--ink)}
.ph{position:absolute}

/* nav */
.nav{position:absolute;left:90px;top:23px;width:998px;height:55px;background:#fff;border-radius:2px}
.brand{position:absolute;left:33px;top:10px;display:flex;align-items:center;gap:8px;font-family:"Exo 2",sans-serif;font-weight:800;font-size:28px;color:var(--ink)}
.brand i{display:block;width:14px;height:14px;background:var(--orange)}
.nav a{position:absolute;top:20px;font-size:12px;color:var(--ink);text-decoration:none;text-transform:uppercase}
.nav .btn{top:8px;height:41px;width:139px;left:850px}

/* hero */
.hero{top:0;height:570px}
.hero-bg{left:0;top:0;width:1200px;height:570px;background:linear-gradient(90deg,#2b1a13 0%,#5e3322 40%,#7a4029 65%,#2a1c16 100%)}
.hero-shade{position:absolute;left:0;top:0;width:700px;height:570px;background:linear-gradient(90deg,rgba(0,0,0,.55),rgba(0,0,0,0))}
.hero .eyebrow{left:112px;top:232px;font-size:24px;color:#fff;letter-spacing:1px}
.hero h1{left:112px;top:262px;font-size:46px;color:#fff;letter-spacing:1px}
.hero p{left:112px;top:322px;width:480px;font-size:14px;line-height:22px;color:#fff}
.dots{left:575px;top:530px;display:flex;gap:6px}
.dots span{width:12px;height:12px;border-radius:50%;border:2px solid #fff;background:#fff}
.dots span:first-child{background:var(--yellow);border-color:var(--yellow)}

/* about */
.about{top:570px;height:439px}
.video{left:112px;top:69px;width:475px;height:302px;background:radial-gradient(circle at 45% 55%,#f2a23a 0%,#b35c1c 35%,#3b2213 75%,#1c120c 100%)}
.play{position:absolute;left:214px;top:128px;width:46px;height:46px;border-radius:50%;background:#fff}
.play:after{content:"";position:absolute;left:19px;top:14px;border-left:13px solid var(--orange);border-top:9px solid transparent;border-bottom:9px solid transparent}
.about .kicker{left:612px;top:67px;font-size:13px;color:#555}
.about h2{left:612px;top:86px;font-size:44px;line-height:49px;font-weight:700;width:470px}
.about p{left:612px;top:195px;width:475px;font-size:13.5px;line-height:24px;color:var(--text)}

/* why */
.why{top:1009px;height:417px;background:linear-gradient(90deg,#4a2212,#2e140a 50%,#3d1b0d)}
.why h2{left:0;width:1200px;text-align:center;top:70px;font-size:42px;font-weight:700;color:#fff}
.feat{position:absolute;top:177px;width:310px;color:#fff}
.feat .icon{width:70px;height:72px;border-radius:10px;background:linear-gradient(135deg,#f0a23a,#d94a2a)}
.feat h3{font-family:"Exo 2",sans-serif;font-size:18px;font-weight:600;margin-top:26px}
.feat p{font-size:13px;line-height:22px;margin-top:6px;color:#f1e6e0}

/* menu */
.menu{top:1426px;height:731px}
.menu h2{left:0;width:1200px;text-align:center;top:58px;font-size:44px;font-weight:700}
.menu .sub{left:0;width:1200px;text-align:center;top:112px;font-size:14px;color:#555}
.dish{position:absolute;width:309px}
.dish .ph{position:relative;width:309px;height:210px}
.dish span{display:block;text-align:center;margin-top:16px;font-family:"Exo 2",sans-serif;font-weight:600;font-size:17px;text-transform:uppercase}

/* gift */
.gift{top:2157px;height:446px;background:linear-gradient(135deg,#2b2b30,#1b1b1f 60%,#26262a)}
.gift-left{left:0;top:0;width:370px;height:446px;background:linear-gradient(90deg,#5a4a2a 0%,#b08a3a 35%,#7a5a30 60%,rgba(40,40,44,0) 100%)}
.gift-right{left:840px;top:110px;width:360px;height:336px;background:linear-gradient(160deg,#1a1a1a 0%,#4a3a28 55%,#b89078 100%)}
.gift .kicker{left:0;width:1200px;text-align:center;top:136px;font-family:"Exo 2",sans-serif;font-weight:700;font-size:17px;color:#fff}
.gift .kicker b{color:var(--yellow);font-weight:700}
.gift h2{left:370px;width:460px;text-align:center;top:160px;font-size:56px;color:#fff;white-space:nowrap}
.gift h2 em{font-style:normal;color:var(--teal)}
.gift p{left:0;width:1200px;text-align:center;top:231px;font-size:13px;color:#fff}

/* hours */
.hours{top:2603px;height:527px}
.hours-card{left:112px;top:68px;width:976px;height:390px;background:#fff;box-shadow:0 0 14px rgba(0,0,0,.12)}
.hours-img{left:0;top:0;width:641px;height:390px;background:linear-gradient(135deg,#3a3028,#1f1a16 60%,#2d2620)}
.hours-img .k{left:31px;top:130px;font-size:13px;color:#fff}
.hours-img h2{left:31px;top:147px;font-size:35px;color:#fff}
.hours-img p{left:31px;top:194px;font-size:13px;color:#fff}
.hours-info{left:682px;top:0;width:270px}
.hours-info h3{position:absolute;font-family:"Exo 2",sans-serif;font-size:20px;font-weight:600;color:var(--ink);white-space:nowrap}
.hours-info h3 b{color:var(--orange);font-weight:600}
.hours-info .row{position:absolute;font-size:12px;color:#333;white-space:nowrap}
.hours-info hr{position:absolute;left:0;width:270px;border:0;border-top:1px dashed #bbb}

/* stats */
.stats{top:3130px;height:244px;background:linear-gradient(90deg,#222,#161616 50%,#222)}
.stat{position:absolute;top:92px;width:260px;text-align:center;color:#fff}
.stat b{display:block;font-family:"Exo 2",sans-serif;font-size:40px;font-weight:600;line-height:40px}
.stat b em{font-style:normal;color:var(--orange)}
.stat span{display:block;margin-top:6px;font-size:13px;letter-spacing:3px}

/* take out */
.takeout{top:3374px;height:449px}
.takeout h2{left:112px;top:108px;font-size:44px;font-weight:700}
.takeout p{left:112px;top:176px;width:470px;font-size:13.5px;line-height:24px;color:var(--text)}
.takeout .order{left:251px;top:289px;font-size:13px;color:var(--ink);line-height:20px}
.takeout .order b{font-weight:600}
.takeout .order b em{font-style:normal;color:var(--orange)}
.shadow{left:626px;top:80px;width:476px;height:303px;background:#d9d9d9}
.photo{left:612px;top:68px;width:476px;height:303px;background:linear-gradient(135deg,#8a6a4a,#c99868 45%,#6f5a48)}

/* newsletter */
.footer{top:4180px;height:465px;background:var(--dark)}
.news{left:112px;top:3823px;width:976px;height:401px;border-radius:10px;background:linear-gradient(135deg,#2b2b2b,#1a1a1a)}
.news .pz{left:0;top:210px;width:440px;height:191px;border-radius:0 0 0 10px;background:linear-gradient(180deg,rgba(26,26,26,0) 0%,#7c3a18 60%,#a8582a 100%)}
.news .k{left:0;width:976px;text-align:center;top:114px;font-size:13px;color:#fff;letter-spacing:1px}
.news h2{left:0;width:976px;text-align:center;top:133px;font-size:42px;font-weight:700;color:#fff}
.news p{left:0;width:976px;text-align:center;top:186px;font-size:13px;color:#ccc}
.field{left:240px;top:242px;width:381px;height:40px;background:#fff;font-size:11px;color:#333;padding:13px 14px}
.news .btn{left:628px;top:242px;width:108px;height:40px}

/* footer */
.col{position:absolute;top:101px}
.col h4{font-family:"Exo 2",sans-serif;font-size:17px;font-weight:700;color:#fff;text-transform:uppercase;margin-bottom:10px}
.col h4 b{color:var(--orange);font-weight:700}
.col a{display:block;font-size:12.5px;color:#ccc;text-decoration:none;line-height:31px}
.col .ln{display:flex;align-items:center;gap:8px;font-size:12.5px;color:#ccc;line-height:36px}
.col .note{font-size:12px;color:#bbb;line-height:19px;width:250px}
.insta{display:grid;grid-template-columns:repeat(3,84px);grid-auto-rows:66px;gap:4px}
.insta div{background:linear-gradient(135deg,#a8562d,#e0a060)}
.insta div:nth-child(2n){background:linear-gradient(135deg,#6b4a35,#c58552)}
.foot-brand{left:0;width:1200px;text-align:center;top:360px;font-family:"Exo 2",sans-serif;font-size:24px;font-weight:800;color:#fff}
.copy{left:0;width:1200px;text-align:center;top:411px;font-size:11.5px;color:#aaa}
.copy b{color:#fff;font-weight:500}
</style>
</head>
<body>

<section class="section hero">
  <div class="ph hero-bg" role="img" aria-label="Photo of the brick restaurant storefront on a street corner"></div>
  <div class="hero-shade"></div>
  <nav class="nav">
    <div class="brand"><i></i>BRAVA</div>
    <a style="left:379px">Menu</a>
    <a style="left:471px">Reservations</a>
    <a style="left:618px">Order Online</a>
    <a style="left:767px">Contact</a>
    <span class="btn">Reservation</span>
  </nav>
  <div class="abs display eyebrow">LETS GET</div>
  <h1 class="abs display">LUNCH AT BRAVA!</h1>
  <p class="abs">If you use this site regularly and would like to help keep the site on the Internet</p>
  <span class="btn" style="left:112px;top:377px;width:132px;height:40px">Book a Table</span>
  <span class="btn light" style="left:258px;top:377px;width:137px;height:40px">Order Online</span>
  <div class="abs dots"><span></span><span></span><span></span></div>
</section>

<section class="section about">
  <div class="ph video" role="img" aria-label="Flames inside the stone oven with a pizza peel"><div class="play"></div></div>
  <div class="abs kicker">Welcome To</div>
  <h2 class="abs head">Brava Stone Oven Kitchen</h2>
  <p class="abs">Sed ut perspiciatis unde omnis iste natus error sit voluptatem accusantium doloremque laudantium, totam rem aperiam, eaque ipsa quae ab illo inventore veritatis et quasi architecto beatae vitae dicta sunt explicabo. Nemo enim ipsam voluptatem quia voluptas sit aspernatur aut odit aut fugit.</p>
  <span class="btn" style="left:612px;top:330px;width:126px;height:40px">Read More</span>
</section>

<section class="section why">
  <h2 class="abs head">Why People Choose Us</h2>
  <div class="feat" style="left:112px"><div class="icon" role="img" aria-label="Burger and fries illustration"></div><h3>Menu For Every Taste</h3><p>Neque porro quisquam est, qui dolorem ipsum quia dolor</p></div>
  <div class="feat" style="left:446px"><div class="icon" role="img" aria-label="Fresh ingredients illustration"></div><h3>Always Fresh Ingredients</h3><p>Neque porro quisquam est, qui dolorem ipsum quia dolor</p></div>
  <div class="feat" style="left:780px"><div class="icon" role="img" aria-label="Chef illustration"></div><h3>Experienced Chefs</h3><p>Neque porro quisquam est, qui dolorem ipsum quia dolor</p></div>
</section>

<section class="section menu">
  <h2 class="abs head">Our Menu</h2>
  <div class="abs sub">Neque porro quisquam est, qui dolorem ipsum quia dolor</div>
  <div class="dish" style="left:112px;top:157px"><div class="ph" role="img" aria-label="Bowls of dips and shareable plates" style="background:linear-gradient(135deg,#4a4a3a,#9a8a4a 50%,#3a3530)"></div><span>Shareables</span></div>
  <div class="dish" style="left:446px;top:157px"><div class="ph" role="img" aria-label="Stone oven pizza on a board" style="background:linear-gradient(135deg,#c99a5a,#e8c890 50%,#8a5a30)"></div><span>Wood Fired Pizza</span></div>
  <div class="dish" style="left:780px;top:157px"><div class="ph" role="img" aria-label="Fresh green salad bowl" style="background:linear-gradient(135deg,#3a4a2a,#7aa04a 50%,#2a2a2a)"></div><span>Salad</span></div>
  <div class="dish" style="left:112px;top:422px"><div class="ph" role="img" aria-label="Toasted sandwich with pickles" style="background:linear-gradient(135deg,#b08a5a,#e0c080 50%,#6a5a3a)"></div><span>Sandwiches</span></div>
  <div class="dish" style="left:446px;top:422px"><div class="ph" role="img" aria-label="Burger with avocado" style="background:linear-gradient(135deg,#a06a3a,#d8a060 45%,#5a7a3a)"></div><span>Burgers</span></div>
  <div class="dish" style="left:780px;top:422px"><div class="ph" role="img" aria-label="Plated main course with pasta" style="background:linear-gradient(135deg,#3a3a3a,#a07060 50%,#2a2a2a)"></div><span>Main &amp; Pasta</span></div>
</section>

<section class="section gift">
  <div class="ph gift-left" role="img" aria-label="Pizza with mushrooms and tomatoes on a yellow band"></div>
  <div class="ph gift-right" role="img" aria-label="Gift voucher card held up in a hand"></div>
  <div class="abs kicker">SPECIAL <b>OCCASION</b></div>
  <h2 class="abs display"><em>GIFT</em> VOUCHER</h2>
  <p class="abs">Neque porro quisquam est qui dolorem ipsum...</p>
  <span class="btn" style="left:540px;top:271px;width:124px;height:39px">Collect Card</span>
</section>

<section class="section hours">
  <div class="abs hours-card">
    <div class="ph hours-img" role="img" aria-label="Dim restaurant interior with bar seating">
      <div class="abs k">About Our</div>
      <h2 class="abs display">WORKING HOURS</h2>
      <p class="abs">Neque porro quisquam est, qui dolorem ipsum quia dolor</p>
      <span class="btn" style="left:31px;top:231px;width:137px;height:37px">Book a Table</span>
    </div>
    <div class="abs hours-info">
      <h3 style="top:30px"><b>Summer Holiday</b> Hours!</h3>
      <div class="row" style="top:72px">Thursday, July 1st &nbsp;- &nbsp;Open</div>
      <div class="row" style="top:101px">Friday, July 2nd &nbsp;- &nbsp;Open</div>
      <div class="row" style="top:128px">Saturday, July 3rd &nbsp;- &nbsp;Open</div>
      <div class="row" style="top:157px">Sunday, July 4th &nbsp;- &nbsp;Closed</div>
      <hr style="top:190px">
      <h3 style="top:205px"><b>Takeout</b> &amp; Kitchen Hours</h3>
      <div class="row" style="top:240px">Thursday to Sunday: 12:00pm - 8:00pm</div>
      <hr style="top:274px">
      <h3 style="top:288px"><b>Outdoor</b> Dining Hours</h3>
      <div class="row" style="top:322px">Our courtyard is open:</div>
      <div class="row" style="top:343px">Thursday to Sunday - 12:00pm - 9:00pm</div>
    </div>
  </div>
</section>

<section class="section stats">
  <div class="stat" style="left:94px"><b><em>1</em>500</b><span>DAILY VISITOR</span></div>
  <div class="stat" style="left:345px"><b><em>3</em>00</b><span>DELIVERIES MONTHLY</span></div>
  <div class="stat" style="left:596px"><b><em>1</em>00%</b><span>POSITIVE FEEDBACK</span></div>
  <div class="stat" style="left:847px"><b><em>4</em>0</b><span>AWARDS AND HONORS</span></div>
</section>

<section class="section takeout">
  <h2 class="abs head">Take Out</h2>
  <p class="abs">Sed ut perspiciatis unde omnis iste natus error sit voluptatem accusantium doloremque laudantium, totam rem aperiam, eaque ipsa quae ab illo inventore veritatis et quasi architecto beatae vitae dicta sunt explicabo.</p>
  <span class="btn" style="left:112px;top:288px;width:124px;height:40px">Read More</span>
  <div class="abs order">Your Order<br><b>Call Us: <em>555-014-2290</em></b></div>
  <div class="ph shadow"></div>
  <div class="ph photo" role="img" aria-label="Guest enjoying a slice of pizza from a takeout box"></div>
</section>

<footer class="section footer">
  <div class="col" style="left:112px">
    <h4><b>S</b>itemap</h4>
    <a>Menu</a><a>Reservation</a><a>Online Booking</a><a>Contact Us</a>
  </div>
  <div class="col" style="left:309px">
    <h4><b>D</b>inner</h4>
    <a>Shareables</a><a>Wood fired pizza</a><a>Salad</a><a>sandwiches</a><a>Burgers</a><a>Main &amp; Pasta</a>
  </div>
  <div class="col" style="left:522px">
    <h4><b>G</b>et in Touch</h4>
    <div class="ln"><svg width="10" height="12" viewBox="0 0 10 12"><path d="M2 1l2 2-1 2 2 3 2-1 2 2-2 2C3 10 0 5 1 2z" fill="#e8501f"/></svg>555-014-2290</div>
    <div class="ln"><svg width="12" height="9" viewBox="0 0 12 9"><rect width="12" height="9" rx="1" fill="#e8501f"/><path d="M0 0l6 5 6-5" stroke="#1f1f1f" fill="none"/></svg>hello@bravalinwell.example</div>
    <h4 style="margin-top:20px"><b>R</b>eservation</h4>
    <div class="note">Reservations will not be available for the courtyard Under phase 1 and 2 of reopening. Walk-ins only. We can't wait to see you!</div>
  </div>
  <div class="col" style="left:829px">
    <h4><b>I</b>nstagram</h4>
    <div class="insta" role="img" aria-label="Grid of six food and guest photos from the restaurant feed">
      <div></div><div></div><div></div><div></div><div></div><div></div>
    </div>
  </div>
  <div class="abs foot-brand">BRAVA</div>
  <div class="abs copy">COPYRIGHT © 2021 <b>BRAVA STONE OVEN KITCHEN</b>. ALL RIGHTS RESERVED.</div>
</footer>

<div class="abs news">
  <div class="ph pz" role="img" aria-label="Pizza on dark stone surface"></div>
  <div class="abs k">NEWSLETTER</div>
  <h2 class="abs head">Subscribe Our Newsletter</h2>
  <p class="abs">Dolorem, beatae dolorum, praesentium itaque et quam quaerat.</p>
  <div class="abs field">Enter Your Email</div>
  <span class="btn">Subscribe</span>
</div>

</body>
</html>
```